2 x Digitize Logo | 2 x Business Cards | 2 x Fridge Magnets

We require 6 deliverables:
1. Residential logo redrawn (same just high quality for large print format).
2. Corporate logo redrawn (minor changes to wording and high quality for large print format).
3. New business card design for Furniture Removals (residential)
4. New business card design for Corporate Relocations (business)
5. New Fridge magnet for Furniture removals (residential)
6. New fridge magnet for Corporate Relocations (business)
1. Residential Logo
a. We require the logo to be translated into a high quality digital image with no modifications.
(see attached resilogo.jpg)
2. Residential Logo
a. We require the logo to be edited (add the word corporate relocations) be translated into a high quality digital image.
(see attached corplogo.jpg)
3. Using the resilogo please make a new business card for our business.
a. Please see the web site https://www.bluegatehaulage.com.au for colours and inspiration.
b. The residential business card needs the following information:
i. Business Name (using the residential logo).
ii. Free Call: 1800 BG Haul (the B, G and Haul much be the same colour as the logo).
iii. Website: www.BluegateHaulage.com.au
iv. Address: 4/6 Marlow Court, VIC 3201
v. Email: move@BluegateHaulage.com.au
vi. backof Card:
Review our service
www.TellTallyHub.com.au
Services: Local, Country, Interstate | Furniture Removals | Piano, Billiard Tables & Antiques
4. Using the corplogo please make a new business card for our business.
b. The corporate business card needs the following information:
i. Business Name (using the corporate logo).
v. Email: corporate@BluegateHaulage.com.au
vi. Back of Card:
Review our service
www.TellTallyHub.com.au
Services: Corporate relocations | Office equipment moves | Packing Service | Packing Materials
5. Using the resilogo please make a new fridge magent for our business.
b. The residential fidge magnet needs the following information:
iv. Services: Local, Country, Interstate | Furniture Removals | Piano, Billiard Tables & Antiques
6. Using the corplogo please make a new fridge magent for our business.
b. The corporate fidge magnet needs the following information:
iv. Services: Local, Country, Interstate | Corporate relocations
Target Market(s)
Residential Furniture Removals and Corporate Office relocations
Industry/Entity Type
Business
Contact Information for Business Card
Please see full brief for six items required
Requirements
Must have
- Clean simple, easy to read
Nice to have
- fresh, stand out, eye catching
Should not have
- plain, standard, boring, general

```html
<!DOCTYPE html>
<html lang="en">
<head>
<meta charset="utf-8">
<title>Bluegate Haulage – Logos, Business Cards and Fridge Magnets</title>
<link rel="stylesheet" href="https://fonts.googleapis.com/css2?family=Open+Sans:wght@400;600;700&display=swap">
<style>
  :root {
    --canvas: #e4e4e2;
    --card: #f4f4f3;
    --card-band: #fbfbfa;
    --card-body: #e9e9e8;
    --ink: #1f1f1f;
    --ink-soft: #3a3a3a;
    --green: #2e8b2e;
    --red: #e0201c;
    --yellow: #f2e300;
    --white: #ffffff;
    --rule: #cfcfcd;
  }
  * { box-sizing: border-box; margin: 0; padding: 0; }
  html, body { width: 1200px; height: 1117px; overflow: hidden; }
  body {
    background: var(--canvas);
    font-family: "Open Sans", Arial, sans-serif;
    color: var(--ink);
    position: relative;
  }
  .wordmark { font-weight: 700; letter-spacing: 0.5px; white-space: nowrap; }
  .wordmark--green { color: var(--green); }
  .wordmark--red { color: var(--red); }
  .mark-dot { display: inline-block; border-radius: 50%; vertical-align: middle; }

  /* Logos */
  .logo { position: absolute; display: flex; align-items: center; justify-content: center; gap: 12px; }
  .logo--residential { left: 100px; top: 160px; width: 384px; height: 80px; font-size: 38px; }
  .logo--corporate { left: 700px; top: 150px; width: 350px; height: 100px; font-size: 38px; }
  .logo .mark-dot { width: 22px; height: 22px; }
  .logo--residential .mark-dot { background: var(--yellow); }
  .logo--corporate .mark-dot { background: var(--green); }

  /* Fridge magnets */
  .magnet { position: absolute; border-radius: 50%; display: flex; flex-direction: column; align-items: center; text-align: center; }
  .magnet--residential {
    left: 188px; top: 406px; width: 204px; height: 204px;
    background: var(--white);
    box-shadow: 0 0 0 8px var(--red), 0 0 0 15px var(--yellow), 0 0 0 20px var(--green);
    padding-top: 34px;
  }
  .magnet--corporate {
    left: 774px; top: 382px; width: 208px; height: 208px;
    background: radial-gradient(circle at 50% 55%, #ffffff 60%, #ececec 100%);
    padding-top: 50px;
  }
  .magnet__ring { position: absolute; inset: -4px; width: 216px; height: 216px; }
  .magnet .wordmark { font-size: 15px; }
  .magnet__free { font-size: 13px; color: var(--ink-soft); margin-top: 3px; }
  .magnet__phone { font-size: 22px; font-weight: 600; line-height: 1.15; }
  .magnet__web { font-size: 8.5px; font-weight: 600; margin-top: 2px; }
  .magnet__services { font-size: 7.5px; color: var(--ink-soft); line-height: 1.7; margin-top: 4px; }
  .magnet__services .rule { display: block; width: 90px; height: 1px; background: var(--red); margin: 1px auto; }
  .magnet--corporate .wordmark { margin-top: 8px; font-size: 12px; }

  .hl-yellow { color: var(--yellow); }
  .hl-red { color: var(--red); }
  .hl-green { color: var(--green); }

  /* Business cards */
  .card { position: absolute; width: 404px; height: 224px; background: var(--card-body); border: 1px solid var(--rule); overflow: hidden; }
  .card--res-front { left: 88px; top: 632px; }
  .card--res-back { left: 88px; top: 878px; }
  .card--corp-front { left: 690px; top: 620px; }
  .card--corp-back { left: 690px; top: 866px; }

  .card__band { background: var(--card-band); border-bottom: 1px solid var(--rule); }
  .card__body { text-align: center; color: var(--ink-soft); }

  .card--res-front .card__band { height: 124px; text-align: center; padding-top: 22px; }
  .card--res-front .wordmark { font-size: 27px; }
  .card--res-front .card__free { font-size: 28px; margin-top: 12px; line-height: 1; }
  .card--res-front .card__free strong { font-weight: 700; }
  .card--res-front .card__body { font-size: 15px; line-height: 30px; padding-top: 4px; }

  .card--corp-front .card__band { height: 130px; display: flex; align-items: center; padding: 0 16px; gap: 18px; }
  .card--corp-front .card__band .wordmark { font-size: 15px; width: 140px; text-align: center; white-space: normal; line-height: 1.2; }
  .card--corp-front .card__contact { flex: 1; }
  .card--corp-front .card__free-label { font-size: 28px; color: var(--ink-soft); line-height: 1.2; }
  .card--corp-front .card__phone { font-size: 30px; font-weight: 700; line-height: 1.15; }
  .card--corp-front .card__web { font-size: 13px; margin-top: 4px; }
  .card--corp-front .card__body { font-size: 17px; line-height: 34px; padding-top: 20px; }

  .card--back { text-align: center; }
  .card--back .wordmark { display: block; margin-top: 26px; }
  .card--res-back .wordmark { font-size: 26px; }
  .card--corp-back .wordmark { font-size: 18px; }
  .card__review { font-size: 16px; letter-spacing: 1px; margin-top: 14px; color: var(--ink-soft); text-transform: uppercase; }
  .card__review-url { font-size: 17px; font-weight: 700; color: var(--ink); }
  .card__services { font-size: 12.5px; color: var(--ink-soft); line-height: 1.6; margin-top: 8px; letter-spacing: 0.5px; }
</style>
</head>
<body>

  <!-- Residential logo -->
  <div class="logo logo--residential">
    <span class="mark-dot"></span>
    <span class="wordmark wordmark--green">Bluegate Haulage</span>
  </div>

  <!-- Corporate logo -->
  <div class="logo logo--corporate">
    <span class="mark-dot"></span>
    <span class="wordmark wordmark--red">Bluegate Haulage</span>
  </div>

  <!-- Residential fridge magnet -->
  <div class="magnet magnet--residential">
    <span class="wordmark wordmark--green">Bluegate Haulage</span>
    <div class="magnet__free">FREE CALL</div>
    <div class="magnet__phone">1800 <span class="hl-yellow">B</span><span class="hl-red">G</span> Haul</div>
    <div class="magnet__web">www.BluegateHaulage.com.au</div>
    <div class="magnet__services">
      Local • Country • Interstate
      <span class="rule"></span>
      Furniture Removals<br>
      Piano, Billiard Tables<br>&amp; Antiques
    </div>
  </div>

  <!-- Corporate fridge magnet -->
  <div class="magnet magnet--corporate">
    <svg class="magnet__ring" viewBox="0 0 216 216" aria-hidden="true">
      <circle cx="108" cy="108" r="104" fill="none" stroke="#d8d8d8" stroke-width="2"/>
      <path d="M 8 108 A 100 100 0 0 1 208 108" fill="none" stroke="var(--green)" stroke-width="6"/>
      <path d="M 14 108 A 94 94 0 0 1 202 108" fill="none" stroke="var(--yellow)" stroke-width="6"/>
      <path d="M 20 108 A 88 88 0 0 1 196 108" fill="none" stroke="var(--red)" stroke-width="5"/>
    </svg>
    <div class="magnet__free">FREE CALL</div>
    <div class="magnet__phone">1800 <span class="hl-red">BG</span> Haul</div>
    <div class="magnet__web">www.BluegateHaulage.com.au</div>
    <div class="magnet__services">
      Local • Country • Interstate
      <span class="rule"></span>
      Corporate relocations
    </div>
    <span class="wordmark wordmark--red">Bluegate Haulage</span>
  </div>

  <!-- Residential business card: front -->
  <section class="card card--res-front">
    <div class="card__band">
      <span class="wordmark wordmark--green">Bluegate Haulage</span>
      <div class="card__free">Free Call <strong>1800 <span class="hl-yellow">B</span><span class="hl-red">G</span> Haul</strong></div>
    </div>
    <div class="card__body">
      <div>www.BluegateHaulage.com.au</div>
      <div>4/6 Marlow Court, VIC 3201</div>
      <div>move@BluegateHaulage.com.au</div>
    </div>
  </section>

  <!-- Residential business card: back -->
  <section class="card card--back card--res-back">
    <span class="wordmark wordmark--green">Bluegate Haulage</span>
    <div class="card__review">Review our service</div>
    <div class="card__review-url">www.TellTallyHub.com.au</div>
    <div class="card__services">
      Local • Country • Interstate<br>
      Furniture Removals | Piano, Billiard Tables &amp; Antiques
    </div>
  </section>

  <!-- Corporate business card: front -->
  <section class="card card--corp-front">
    <div class="card__band">
      <span class="wordmark wordmark--red">Bluegate Haulage</span>
      <div class="card__contact">
        <div class="card__free-label">Free Call</div>
        <div class="card__phone">1800 <span class="hl-red">BG</span> Haul</div>
        <div class="card__web">www.BluegateHaulage.com.au</div>
      </div>
    </div>
    <div class="card__body">
      <div>4/6 Marlow Court, VIC 3201</div>
      <div>corporate@BluegateHaulage.com.au</div>
    </div>
  </section>

  <!-- Corporate business card: back -->
  <section class="card card--back card--corp-back">
    <span class="wordmark wordmark--red">Bluegate Haulage</span>
    <div class="card__review">Review our service</div>
    <div class="card__review-url">www.TellTallyHub.com.au</div>
    <div class="card__services">
      Local • Country • Interstate<br>
      Corporate relocations | Office equipment moves<br>
      Packing Service | Packing Materials
    </div>
  </section>

</body>
</html>
```